Spray Foam Company Business Card

We need a business card designed for our spray foam insulation and roof coatings business. We handle residential and commercial projects.
Industry/Entity Type
Construction
Contact Information for Business Card
We would like it to say:
K & R Coat
with these bullet points
-foam insulation
-waterproofing roof system
-water proofing foundation systems
website is krcoatfoamsealers.com (this was just purchased)
office phone : 630-555-0148
And 3 cards with names on them the names are :
Darren Hollis
Trevor Lindqvist
Neil Bruxton
maybe the bullet points can go on the back?
if you go this website it is another division of our company and you can see the font we use in the K & R. We do not want to use the same half circles that it has just the lettering
www.thesturdiestfinishwork.com
Look and feel
Each slider illustrates characteristics of the customer's brand and the style your logo design should communicate.

```html
<!DOCTYPE html>
<html lang="en">
<head>
<meta charset="utf-8">
<title>K &amp; R Coat — Business Card</title>
<link rel="stylesheet" href="https://fonts.googleapis.com/css2?family=Jost:wght@400;500&display=swap">
<style>
  :root {
    --navy: #28275f;
    --navy-deep: #1f1e52;
    --red: #cf3138;
    --orange: #ee8650;
    --amber: #e9b13a;
    --yellow: #d8c82b;
    --ink: #1d1c3a;
    --white: #f4f4f6;
    --stage: #e9e6e0;
    --card-w: 900px;
    --card-h: 514px;
  }
  * { box-sizing: border-box; margin: 0; padding: 0; }
  html, body { width: 1200px; height: 1200px; overflow: hidden; }
  body {
    background: var(--stage);
    font-family: "Jost", "Futura", sans-serif;
    position: relative;
  }
  .card {
    position: absolute;
    left: 150px;
    width: var(--card-w);
    height: var(--card-h);
    background: var(--navy);
    overflow: hidden;
    box-shadow: 0 10px 28px rgba(0,0,0,.22);
  }
  .card--contact { top: 60px; }
  .card--services { top: 626px; }
  .card__band { position: absolute; inset: 0; width: 100%; height: 100%; }

  .wordmark {
    position: absolute;
    font-weight: 500;
    font-size: 58px;
    letter-spacing: 1px;
    white-space: nowrap;
  }
  .card--contact .wordmark { top: 44px; right: 60px; color: var(--white); }
  .card--services .wordmark { top: 92px; left: 0; right: 0; text-align: center; color: var(--ink); }

  .person { position: absolute; left: 62px; top: 158px; }
  .person__name { color: var(--white); font-size: 21px; }
  .person__role { color: var(--amber); font-size: 21px; margin-top: 2px; }

  .contact-list { position: absolute; left: 62px; top: 258px; list-style: none; }
  .contact-list li {
    display: flex; align-items: center; gap: 18px;
    color: var(--white); font-size: 21px; line-height: 30px;
  }
  .contact-list svg { width: 20px; height: 20px; fill: var(--amber); flex: none; }

  .address {
    position: absolute; right: 44px; top: 290px; text-align: right;
    color: var(--ink); font-size: 19px; line-height: 26px;
  }
  .address__company { font-weight: 500; }

  .card--contact .website {
    position: absolute; left: 62px; bottom: 42px;
    color: var(--ink); font-size: 19px; letter-spacing: .5px;
  }

  .services { position: absolute; left: 92px; top: 358px; list-style: none; }
  .services li {
    display: flex; align-items: center; gap: 14px;
    color: var(--white); font-size: 23px; line-height: 33px;
  }
  .services svg { width: 24px; height: 14px; flex: none; }

  .card--services .website {
    position: absolute; right: 120px; bottom: 78px;
    color: var(--yellow); font-size: 22px; letter-spacing: 1px;
  }
</style>
</head>
<body>

<section class="card card--contact" aria-label="Business card, contact side">
  <svg class="card__band" viewBox="0 0 900 514" preserveAspectRatio="none" aria-hidden="true">
    <defs>
      <linearGradient id="band-contact" x1="0" y1="0" x2="1" y2="0">
        <stop offset="0" stop-color="#cf3138"/>
        <stop offset=".3" stop-color="#ee8650"/>
        <stop offset=".65" stop-color="#e9b13a"/>
        <stop offset="1" stop-color="#d8c82b"/>
      </linearGradient>
    </defs>
    <path d="M0 330 C150 318 280 300 420 282 C560 262 640 220 760 190 C820 176 860 168 900 160 V514 H0 Z" fill="url(#band-contact)"/>
  </svg>

  <div class="wordmark">K &amp; R Coat</div>

  <div class="person">
    <p class="person__name">Darren Hollis</p>
    <p class="person__role">CEO</p>
  </div>

  <ul class="contact-list">
    <li>
      <svg viewBox="0 0 20 20" aria-label="Mobile"><path d="M6 1h8a1 1 0 0 1 1 1v16a1 1 0 0 1-1 1H6a1 1 0 0 1-1-1V2a1 1 0 0 1 1-1zm1 2v11h6V3zm3 12.5a1 1 0 1 0 0 2 1 1 0 0 0 0-2z"/></svg>
      000-000-0000
    </li>
    <li>
      <svg viewBox="0 0 20 20" aria-label="Office phone"><path d="M2 7c0-2 2-3 8-3s8 1 8 3v1h-4V6.5c-1-.4-2.4-.5-4-.5s-3 .1-4 .5V8H2zm3 2h10l2 8H3zm5 2.5a2.5 2.5 0 1 0 0 5 2.5 2.5 0 0 0 0-5z"/></svg>
      630-555-0148
    </li>
    <li>
      <svg viewBox="0 0 20 20" aria-label="Email"><path d="M1 4h18v12H1zm2 2v.4l7 5 7-5V6zm0 2.8V14h14V8.8l-7 5z"/></svg>
      darren@krcoatfoamsealers.com
    </li>
  </ul>

  <div class="address">
    <p class="address__company">K &amp; R Coat</p>
    <p>212 Meadowlark Lane</p>
    <p>Plainfield, IL 60544</p>
  </div>

  <p class="website">www.krcoatfoamsealers.com</p>
</section>

<section class="card card--services" aria-label="Business card, services side">
  <svg class="card__band" viewBox="0 0 900 514" preserveAspectRatio="none" aria-hidden="true">
    <defs>
      <linearGradient id="band-services" x1="0" y1="0" x2="1" y2="0">
        <stop offset="0" stop-color="#cf3138"/>
        <stop offset=".28" stop-color="#ee8650"/>
        <stop offset=".6" stop-color="#e9b13a"/>
        <stop offset="1" stop-color="#d8c82b"/>
      </linearGradient>
    </defs>
    <path d="M0 0 H900 V232 C780 226 660 222 540 232 C400 246 300 272 180 290 C110 300 50 304 0 306 Z" fill="url(#band-services)"/>
  </svg>

  <div class="wordmark">K &amp; R Coat</div>

  <ul class="services">
    <li><svg viewBox="0 0 24 14" aria-hidden="true"><path d="M0 7 L14 2 L12 6 H24 V8 H12 L14 12 Z" fill="#e9b13a"/></svg>Foam Insulation</li>
    <li><svg viewBox="0 0 24 14" aria-hidden="true"><path d="M0 7 L14 2 L12 6 H24 V8 H12 L14 12 Z" fill="#e9b13a"/></svg>Waterproofing Roof System</li>
    <li><svg viewBox="0 0 24 14" aria-hidden="true"><path d="M0 7 L14 2 L12 6 H24 V8 H12 L14 12 Z" fill="#e9b13a"/></svg>Water Proofing Foundation Systems</li>
  </ul>

  <p class="website">www.krcoatfoamsealers.com</p>
</section>

</body>
</html>
```